Design a visually appealing layout for our company mission and values. I want to create a visually appealing 1 page flyer that presents our company mission and values to clients as well as to our internal team/staff. We will utilize the 1 page flyer in internal and external presentations about our company. We will also use the flyer in sales proposals/marketing packages.

Target Market(s)

Internal team members as well as external prospective clients, existing clients & referral partners

Industry/Entity Type

Financial Service

Colors

Designer to choose colors to be used in the design.

Requirements
Must have
• Should reflect our company brand so I have included our Pantone panel, fonts etc. I have provided our company logo as well which should be part of the branded document
Nice to have
• I would like the presentation to be useable in different formats and to different audiences so something that is more graphic/visual heavy - otherwise it's a lot of words that people don't read.
• Would like to be able to easily include in our corporate template powerpoint presentation.

```html
<!DOCTYPE html>
<html lang="en">
<head>
<meta charset="utf-8">
<title>Mission &amp; Values</title>
<link rel="stylesheet" href="https://fonts.googleapis.com/css2?family=Source+Sans+3:wght@300;400;600;700&display=swap">
<style>
  :root {
    --green: #8dc63f;
    --blue: #1e9ad6;
    --blue-deep: #1880c2;
    --navy: #1b3a5c;
    --royal: #1b6bb0;
    --plum: #5a2a48;
    --taupe: #8b7765;
    --rust: #b0521d;
    --heading: #595959;
    --body: #3f3f3f;
    --rule: #c9c9c9;
    --page: #ffffff;
  }
  * { margin: 0; padding: 0; box-sizing: border-box; }
  html, body { width: 1200px; height: 911px; overflow: hidden; background: var(--page); }
  body { font-family: "Source Sans 3", Arial, sans-serif; }
  .flyer { position: relative; width: 1200px; height: 911px; background: var(--page); }

  .title {
    position: absolute; top: 46px; left: 0; width: 100%;
    text-align: center; font-weight: 300; font-size: 44px;
    color: var(--green); letter-spacing: 1px;
  }
  .mission {
    position: absolute; left: 66px; top: 124px; width: 1060px; height: 56px;
    border-radius: 28px;
    background: linear-gradient(180deg, #37aee3 0%, var(--blue) 55%, var(--blue-deep) 100%);
    box-shadow: 0 10px 14px -8px rgba(0,0,0,0.35);
    color: #fff; font-weight: 600; font-size: 21px; letter-spacing: 0.3px;
    display: flex; align-items: center; justify-content: center;
  }

  .wheel { position: absolute; left: 0; top: 0; width: 1200px; height: 911px; }

  .hub-name {
    position: absolute; left: 459px; top: 484px; width: 280px; text-align: center;
    font-weight: 700; font-size: 44px; color: var(--blue-deep); line-height: 1;
    letter-spacing: 1px;
  }
  .hub-tag {
    position: absolute; left: 459px; top: 563px; width: 280px; text-align: center;
    font-weight: 400; font-size: 34px; color: var(--green); line-height: 1;
  }

  .value-icon {
    position: absolute; width: 82px; height: 82px; border-radius: 50%;
    display: flex; align-items: center; justify-content: center;
    overflow: hidden;
  }
  .value-icon svg { width: 46px; height: 46px; }
  .icon-teamwork { left: 558px; top: 253px; background: var(--blue); }
  .icon-empowerment { left: 735px; top: 325px; background: var(--green); }
  .icon-knowledge { left: 813px; top: 504px; background: var(--navy); }
  .icon-proactivity { left: 735px; top: 679px; background: var(--royal); }
  .icon-dedication { left: 379px; top: 679px; background: var(--plum); }
  .icon-security { left: 305px; top: 504px; background: var(--taupe); }
  .icon-transparency { left: 379px; top: 325px; background: var(--rust); }

  .value { position: absolute; width: 260px; }
  .value h2 {
    font-size: 18px; font-weight: 700; color: var(--heading);
    letter-spacing: 0.2px; line-height: 1.1; margin-bottom: 2px;
  }
  .value p { font-size: 12.5px; line-height: 1.3; color: var(--body); }
  .value.right-side { text-align: left; }
  .value.left-side { text-align: right; }
  .value-teamwork { left: 661px; top: 232px; width: 255px; }
  .value-empowerment { left: 843px; top: 349px; width: 250px; }
  .value-knowledge { left: 919px; top: 521px; width: 255px; }
  .value-proactivity { left: 843px; top: 695px; width: 250px; }
  .value-transparency { left: 83px; top: 349px; }
  .value-security { left: 17px; top: 521px; }
  .value-dedication { left: 83px; top: 695px; }

  .footer-rule {
    position: absolute; left: 80px; top: 826px; width: 1037px; height: 2px;
    background: var(--rule);
  }
  .contact {
    position: absolute; top: 847px; left: 0; width: 100%; text-align: center;
    font-size: 16px; letter-spacing: 1.2px; color: var(--blue-deep);
  }
  .contact .divider { margin: 0 10px; }
</style>
</head>
<body>
<main class="flyer">
  <h1 class="title">MISSION &amp; VALUES</h1>
  <div class="mission">OUR MISSION: TO PROACTIVELY SUPPORT ORGANIZATIONS AND LEAD THEM TOWARD A SECURE FUTURE</div>

  <svg class="wheel" viewBox="0 0 1200 911" aria-hidden="true">
    <defs>
      <radialGradient id="ring-fill" cx="50%" cy="50%" r="50%">
        <stop offset="70%" stop-color="#d6d6d6"/>
        <stop offset="85%" stop-color="#ececec"/>
        <stop offset="100%" stop-color="#f8f8f8"/>
      </radialGradient>
      <filter id="hub-shadow" x="-30%" y="-30%" width="160%" height="160%">
        <feDropShadow dx="4" dy="8" stdDeviation="9" flood-color="#000" flood-opacity="0.3"/>
      </filter>
    </defs>
    <circle cx="599" cy="545" r="190" fill="url(#ring-fill)"/>
    <circle cx="599" cy="545" r="186" fill="none" stroke="#e6e6e6" stroke-width="1.5"/>
    <circle cx="599" cy="545" r="140" fill="#fff" filter="url(#hub-shadow)"/>

    <g stroke="#b9b9b9" stroke-width="1.5">
      <line x1="599" y1="335" x2="599" y2="357"/>
      <line x1="748" y1="396" x2="735" y2="410"/>
      <line x1="813" y1="545" x2="790" y2="545"/>
      <line x1="748" y1="694" x2="735" y2="680"/>
      <line x1="450" y1="694" x2="463" y2="680"/>
      <line x1="387" y1="545" x2="410" y2="545"/>
      <line x1="450" y1="396" x2="463" y2="410"/>
    </g>
    <circle cx="599" cy="359" r="5" fill="var(--blue)"/>
    <circle cx="733" cy="412" r="5" fill="var(--green)"/>
    <circle cx="787" cy="545" r="5" fill="var(--navy)"/>
    <circle cx="733" cy="678" r="5" fill="var(--royal)"/>
    <circle cx="465" cy="678" r="5" fill="var(--plum)"/>
    <circle cx="411" cy="545" r="5" fill="var(--taupe)"/>
    <circle cx="465" cy="412" r="5" fill="var(--rust)"/>
  </svg>

  <div class="hub-name">CALDER</div>
  <div class="hub-tag">WE VALUE</div>

  <div class="value-icon icon-teamwork">
    <svg viewBox="0 0 46 46" fill="#fff" aria-hidden="true">
      <circle cx="12" cy="16" r="4"/><circle cx="23" cy="14" r="5"/><circle cx="34" cy="16" r="4"/>
      <path d="M5 32c0-6 3-9 7-9s7 3 7 9z"/><path d="M27 32c0-6 3-9 7-9s7 3 7 9z"/>
      <path d="M14 34c0-8 4-12 9-12s9 4 9 12z"/>
    </svg>
  </div>
  <div class="value-icon icon-empowerment">
    <svg viewBox="0 0 46 46" fill="#fff" aria-hidden="true">
      <rect x="8" y="30" width="5" height="9"/><rect x="16" y="25" width="5" height="14"/>
      <rect x="24" y="20" width="5" height="19"/><rect x="32" y="14" width="5" height="25"/>
      <path d="M7 26 L20 15 L26 19 L36 9" fill="none" stroke="#fff" stroke-width="2.5"/>
      <path d="M31 7 L39 6 L38 14 Z"/>
    </svg>
  </div>
  <div class="value-icon icon-knowledge">
    <svg viewBox="0 0 46 46" fill="none" stroke="#fff" stroke-width="2" aria-hidden="true">
      <path d="M17 27c-3-2-5-5-5-9a11 11 0 0 1 22 0c0 4-2 7-5 9v4H17z"/>
      <line x1="18" y1="35" x2="28" y2="35"/><line x1="20" y1="39" x2="26" y2="39"/>
      <line x1="23" y1="2" x2="23" y2="5"/><line x1="6" y1="18" x2="3" y2="18"/><line x1="40" y1="18" x2="43" y2="18"/>
      <line x1="10" y1="7" x2="12" y2="9"/><line x1="36" y1="7" x2="34" y2="9"/>
    </svg>
  </div>
  <div class="value-icon icon-proactivity">
    <svg viewBox="0 0 46 46" fill="none" stroke="#fff" stroke-width="2.5" aria-hidden="true">
      <circle cx="23" cy="23" r="16"/><circle cx="23" cy="23" r="10"/>
      <circle cx="23" cy="23" r="3.5" fill="#fff"/>
      <line x1="23" y1="2" x2="23" y2="9"/><line x1="23" y1="37" x2="23" y2="44"/>
      <line x1="2" y1="23" x2="9" y2="23"/><line x1="37" y1="23" x2="44" y2="23"/>
    </svg>
  </div>
  <div class="value-icon icon-dedication">
    <svg viewBox="0 0 46 46" fill="#fff" aria-hidden="true">
      <rect x="7" y="20" width="7" height="18" rx="1"/>
      <path d="M16 21 L23 8 c3 0 4 2 3 6 l-1 4 h10 c3 0 4 3 3 5 l-3 12 c-1 2-2 3-4 3 H16z"/>
    </svg>
  </div>
  <div class="value-icon icon-security">
    <svg viewBox="0 0 46 46" aria-hidden="true">
      <path d="M23 4 L39 10 v11 c0 10-7 17-16 21 C14 38 7 31 7 21 V10z" fill="none" stroke="#fff" stroke-width="2.5"/>
      <rect x="16" y="21" width="14" height="11" rx="1.5" fill="#fff"/>
      <path d="M18.5 21 v-3 a4.5 4.5 0 0 1 9 0 v3" fill="none" stroke="#fff" stroke-width="2.2"/>
    </svg>
  </div>
  <div class="value-icon icon-transparency">
    <svg viewBox="0 0 46 46" aria-hidden="true">
      <ellipse cx="25" cy="9" rx="12" ry="4" fill="#fff"/>
      <path d="M13 9 v18 c0 2 5 4 12 4 s12-2 12-4 V9 c0 2-5 4-12 4 s-12-2-12-4z" fill="#fff"/>
      <circle cx="17" cy="29" r="8" fill="var(--rust)" stroke="#fff" stroke-width="2.5"/>
      <line x1="11" y1="35" x2="4" y2="42" stroke="#fff" stroke-width="3.5" stroke-linecap="round"/>
    </svg>
  </div>

  <section class="value right-side value-teamwork">
    <h2>TEAMWORK</h2>
    <p>Collaborating with team members, clients and partners to maintain a high level of communication, accountability and engagement to achieve our common goals</p>
  </section>
  <section class="value right-side value-empowerment">
    <h2>FINANCIAL EMPOWERMENT</h2>
    <p>We commit ourselves to providing the best retirement solutions to guide our clients toward financial freedom</p>
  </section>
  <section class="value right-side value-knowledge">
    <h2>KNOWLEDGE</h2>
    <p>Our team of highly trained and credentialed experts work to educate and lead our clients toward success</p>
  </section>
  <section class="value right-side value-proactivity">
    <h2>PROACTIVITY</h2>
    <p>We hold ourselves accountable in anticipating regulatory changes and keeping you and your plan in compliance</p>
  </section>
  <section class="value left-side value-transparency">
    <h2>TRANSPARENCY</h2>
    <p>We take pride in representing the retirement plan industry as an open, honest, and socially responsible firm with our clients</p>
  </section>
  <section class="value left-side value-security">
    <h2>SECURITY</h2>
    <p>With an emphasis on high technological standards, we lead you toward peace of mind that your savings and investments are protected</p>
  </section>
  <section class="value left-side value-dedication">
    <h2>DEDICATION</h2>
    <p>We provide exceptional customer service and ensure that we are friendly, timely and responsive whenever corresponding with our clients</p>
  </section>

  <div class="footer-rule"></div>
  <p class="contact">www.calderplan.com<span class="divider">|</span>info@calderplan.com</p>
</main>
</body>
</html>
```